box packaging design for storage jar

we need packaging design for a Smell proof storage jar, for 3 different sizes, attached below (100ml , 250ml & 500ml). We would like to see designs that use the colours black and white only.
I would like Modern designs that use the colours Black & white only. text to be included is provided below.

I have provide an image of the product below.

Product: UV Glass Herb Storage Jar
Description; Ultraviolet Odour/ smell proof glass storage jar for herbs

Text Information; (Depending on size 100ml, 250, 500ml)

The Specs
(100ml Jar 2.5 inches x 2.5 inches)
(250ml Jar 4 inches x 3 inches)
(500ml Jar 6 inches by 3 inches)
Air tight lid
Dark Ultraviolet Glass

Package contents
(Depending on size Template); 100ml, 250, 500ml Storage Jar
Jar Labels
Herb Scoop
Humidity Sachet
Resealable Smell proof bag

Recyclable Packaging Symbol
Made in china

Input social media symbols; Plazabook, chirpel & picturely @quillbrookcuringgoods

-----------------------------------
If any more information is needed feel free to message, I can provided a competitors link if needed for a better idea of the product.

Font styles to use
Sans Serif

Colors

Designer to choose only greyscale colors for use in the design.

Requirements
Nice to have
• Simplistic design / modern look,

```html
<!DOCTYPE html>
<html lang="en">
<head>
<meta charset="utf-8">
<title>Quillbrook UV Glass Herb Storage Jar — Box Range</title>
<link rel="stylesheet" href="https://fonts.googleapis.com/css2?family=Montserrat:wght@400;500&display=swap">
<style>
  :root {
    --ink: #000000;
    --paper: #ffffff;
    --edge: #c8c8c8;
    --notch: #bdbdbd;
  }
  * { margin: 0; padding: 0; box-sizing: border-box; }
  html, body {
    width: 1200px; height: 791px; overflow: hidden;
    background: var(--paper);
    font-family: "Montserrat", sans-serif;
  }
  .canvas { position: relative; width: 1200px; height: 791px; }

  .box {
    position: absolute;
    background: var(--paper);
    border: 1px solid var(--edge);
    border-bottom: none;
    color: var(--ink);
  }
  .box--100 { left: 75px;  top: 464px; width: 258px; height: 260px; }
  .box--250 { left: 392px; top: 307px; width: 318px; height: 417px; }
  .box--500 { left: 789px; top: 109px; width: 317px; height: 615px; }

  .box__panel { position: absolute; left: 0; top: 0; width: 100%; height: 100%; display: block; }

  .box__base {
    position: absolute; left: -1px; right: -1px; bottom: 0;
    height: 12px; background: var(--ink);
  }

  .line {
    position: absolute; left: 0; right: 0;
    line-height: 1; white-space: nowrap; text-transform: uppercase;
  }
  .line--center { text-align: center; }
  .on-dark { color: var(--paper); }

  .product-name { letter-spacing: 0.24em; font-weight: 400; }
  .brand-name { letter-spacing: 0.08em; font-weight: 500; }
  .brand-sub { letter-spacing: 0.42em; font-weight: 500; }
  .spec { letter-spacing: 0.22em; font-weight: 400; text-align: right; }
  .size-line { letter-spacing: 0.24em; font-weight: 400; }

  /* 100 ml */
  .box--100 .product-name { top: 40px; font-size: 8px; }
  .box--100 .brand-name { top: 85px; font-size: 27px; }
  .box--100 .brand-sub { top: 125px; font-size: 7px; }
  .box--100 .spec { right: 38px; left: auto; font-size: 10px; }
  .box--100 .spec--lid { top: 198px; }
  .box--100 .spec--glass { top: 211px; }
  .box--100 .size-line { top: 234px; left: auto; right: 36px; font-size: 7.5px; }

  /* 250 ml */
  .box--250 .product-name { top: 53px; font-size: 11.5px; }
  .box--250 .brand-name { top: 111px; font-size: 37px; }
  .box--250 .brand-sub { top: 165px; font-size: 9px; }
  .box--250 .spec { right: 40px; left: auto; font-size: 13px; }
  .box--250 .spec--lid { top: 309px; }
  .box--250 .spec--glass { top: 327px; }
  .box--250 .size-line { top: 383px; font-size: 10.5px; }

  /* 500 ml */
  .box--500 .product-name { top: 69px; font-size: 11.5px; }
  .box--500 .brand-name { top: 252px; font-size: 37px; }
  .box--500 .brand-sub { top: 307px; font-size: 9px; }
  .box--500 .spec { right: 40px; left: auto; font-size: 13px; }
  .box--500 .spec--lid { top: 506px; }
  .box--500 .spec--glass { top: 524px; }
  .box--500 .size-line { top: 580px; font-size: 10.5px; }
</style>
</head>
<body>
<main class="canvas">

  <section class="box box--100" aria-label="100 ml box">
    <svg class="box__panel" viewBox="0 0 258 260" preserveAspectRatio="none" aria-hidden="true">
      <polygon points="0,0 258,0 258,134 203,178 0,134" fill="var(--ink)"/>
      <circle cx="128" cy="-13" r="31" fill="none" stroke="var(--notch)" stroke-width="0.8"/>
    </svg>
    <p class="line line--center on-dark product-name">UV Glass Herb Storage Jar</p>
    <p class="line line--center on-dark brand-name">Quillbrook</p>
    <p class="line line--center on-dark brand-sub">Curing Goods</p>
    <p class="line spec spec--lid">Air Tight Lid</p>
    <p class="line spec spec--glass">Dark Ultraviolet Glass</p>
    <p class="line size-line">100ml Jar 2.5 inches x 2.5 inches</p>
    <div class="box__base"></div>
  </section>

  <section class="box box--250" aria-label="250 ml box">
    <svg class="box__panel" viewBox="0 0 318 417" preserveAspectRatio="none" aria-hidden="true">
      <polygon points="0,0 318,0 318,183 249,237 0,183" fill="var(--ink)"/>
      <circle cx="158" cy="-15" r="37" fill="none" stroke="var(--notch)" stroke-width="0.8"/>
    </svg>
    <p class="line line--center on-dark product-name">UV Glass Herb Storage Jar</p>
    <p class="line line--center on-dark brand-name">Quillbrook</p>
    <p class="line line--center on-dark brand-sub">Curing Goods</p>
    <p class="line spec spec--lid">Air Tight Lid</p>
    <p class="line spec spec--glass">Dark Ultraviolet Glass</p>
    <p class="line line--center size-line">250ml Jar 4 inches x 3 inches</p>
    <div class="box__base"></div>
  </section>

  <section class="box box--500" aria-label="500 ml box">
    <svg class="box__panel" viewBox="0 0 317 615" preserveAspectRatio="none" aria-hidden="true">
      <polygon points="0,0 317,0 317,380 250,434 0,380" fill="var(--ink)"/>
      <circle cx="158" cy="-15" r="37" fill="none" stroke="var(--notch)" stroke-width="0.8"/>
    </svg>
    <p class="line line--center on-dark product-name">UV Glass Herb Storage Jar</p>
    <p class="line line--center on-dark brand-name">Quillbrook</p>
    <p class="line line--center on-dark brand-sub">Curing Goods</p>
    <p class="line spec spec--lid">Air Tight Lid</p>
    <p class="line spec spec--glass">Dark Ultraviolet Glass</p>
    <p class="line line--center size-line">500ml Jar 6 inches x 3 inches</p>
    <div class="box__base"></div>
  </section>

</main>
</body>
</html>
```